依頼概要
〇依頼の目的/概要
電子書籍(lumora)の表紙デザインをおねがいします。

〇画像サイズ
表紙サイズの理想的な寸法は2560×1600ピクセルです。
注:画像の寸法は1000×625ピクセル以上であることが必要です。
画像の最大の寸法は10000×10000ピクセルです。

〇タイトル
夜更けの庭で青い灯をさがす旅の物語です!

〇帯キャッチ

・眠ることも許されない
死にたくなるようなかゆみと痛みから
柔らかい潤いのある肌になった

・人生の波と家族とのご縁をひもといて
薬を使わずに治す

・「絶対に治る、治ったら
同じように苦しんでいる人の為に役立つ本を書こう」
・・・と決めていました。

デザイナーさんの判断で、
どれかを使ってもらっても、
または全部を使ってもらってもOKです。

〇著者 ぽんたるべカフェ 占導師 千景(柴崎奈緒)

文字の大きさと配置と色のインパクトがあって一目惚れしました。
修正依頼にも迅速な対応もありがたかったです。

初めての電子書籍の執筆と初めてのワークベリーへの仕事依頼で、
ドキドキで、いろいろ小さなわからないところだらけでした。
たくさんの提案、どれも素敵なものばかりですべての提案者の方々に
感謝の氣持ちでいっぱいです。ありがとうございました。
これからもアトピー性皮膚炎を克服するための電子書籍を執筆していく予定なので
また、協力していただけたら嬉しいです。

```html
<!DOCTYPE html>
<html lang="ja">
<head>
<meta charset="utf-8">
<title>夜更けの庭で青い灯をさがす旅の物語です!</title>
<link rel="stylesheet" href="https://fonts.googleapis.com/css2?family=M+PLUS+Rounded+1c:wght@500;800;900&family=Noto+Sans+JP:wght@500;700;900&family=Noto+Serif+JP:wght@600;900&display=swap">
<style>
  :root {
    --bg-top: #dcefc4;
    --bg-mid: #f7fbef;
    --title-orange: #f08a12;
    --title-ink: #1e1e1e;
    --bubble-green: #8cc63f;
    --label-green: #5fa82a;
    --band-orange: #f5a623;
    --box-white: #ffffff;
    --box-line: #8cc63f;
    --text: #222222;
    --figure-hair: #e59a3a;
    --figure-skin: #f7d3b0;
    --figure-shirt: #f0602a;
    --figure-jeans: #3a6ea8;
  }
  html, body { margin: 0; padding: 0; overflow: hidden; }
  body { width: 749px; height: 1200px; }
  .cover {
    position: relative;
    width: 749px; height: 1200px;
    overflow: hidden;
    background: linear-gradient(180deg, var(--bg-top) 0%, var(--bg-mid) 45%, var(--bg-mid) 100%);
    font-family: "Noto Sans JP", sans-serif;
    color: var(--text);
  }
  .figure {
    position: absolute; left: 330px; top: 330px; z-index: 0;
    width: 310px; height: 600px;
    background: linear-gradient(180deg, var(--figure-hair) 0%, var(--figure-skin) 30%, var(--figure-shirt) 55%, var(--figure-shirt) 75%, var(--figure-jeans) 100%);
    border-radius: 155px 155px 20px 20px;
    opacity: .8;
  }
  .title-top {
    position: absolute; left: 0; right: 0; top: 60px; margin: 0; z-index: 1;
    text-align: center;
    font-family: "M PLUS Rounded 1c", sans-serif;
    font-weight: 900; font-size: 100px; line-height: 1.1;
    color: var(--title-orange);
    letter-spacing: 0;
    -webkit-text-stroke: 6px #fff;
    paint-order: stroke fill;
  }
  .bubble {
    position: absolute; left: 115px; top: 235px; z-index: 2;
    width: 180px; height: 140px;
  }
  .bubble svg { position: absolute; inset: 0; }
  .bubble-text {
    position: absolute; inset: 0;
    display: flex; flex-direction: column; align-items: center; justify-content: center;
    font-family: "M PLUS Rounded 1c", sans-serif;
    font-weight: 800; color: #fff; font-size: 33px; line-height: 1.15;
    transform: rotate(-8deg);
    padding-bottom: 14px;
  }
  .title-main {
    position: absolute; left: 300px; top: 195px; width: 440px; z-index: 2;
    font-family: "Noto Sans JP", sans-serif;
    font-weight: 900; font-size: 92px; line-height: 1.1;
    color: var(--title-ink);
    letter-spacing: -2px;
    -webkit-text-stroke: 5px #fff;
    paint-order: stroke fill;
  }
  .author {
    position: absolute; left: 30px; top: 510px; z-index: 2;
    font-weight: 700;
  }
  .author-label {
    display: inline-block;
    background: var(--label-green); color: #fff;
    font-size: 20px; padding: 2px 10px; border-radius: 4px;
  }
  .author-org { font-size: 21px; margin-top: 8px; color: var(--label-green); }
  .author-name { font-size: 28px; margin-top: 4px; color: var(--label-green); }
  .lead-box {
    position: absolute; left: 28px; top: 660px; z-index: 2;
    width: 300px; padding: 14px 18px;
    background: var(--box-white);
    border: 3px solid var(--box-line);
    font-weight: 700; font-size: 26px; line-height: 1.45;
  }
  .lead-box em { font-style: normal; color: var(--label-green); font-size: 30px; }
  .band {
    position: absolute; left: 0; right: 0; top: 930px; bottom: 0; z-index: 3;
    background: var(--band-orange);
    padding: 26px 22px 0;
    font-family: "Noto Serif JP", serif;
    font-weight: 600; color: var(--text);
  }
  .band-lead { font-size: 80px; font-weight: 900; line-height: 1.1; letter-spacing: -2px; white-space: nowrap; }
  .band-lead small { font-size: 36px; font-weight: 600; letter-spacing: 0; }
  .band-line { font-size: 37px; line-height: 1.45; white-space: nowrap; }
  .band-lead + .band-line { margin-top: 10px; }
</style>
</head>
<body>
<main class="cover">
  <div class="figure" role="img" aria-label="Illustration of a woman in an orange top, looking worried and holding her stomach"></div>

  <h1 class="title-top">夜更けの庭で</h1>

  <div class="bubble">
    <svg viewBox="0 0 180 140" width="180" height="140" aria-hidden="true">
      <ellipse cx="90" cy="64" rx="88" ry="58" fill="var(--bubble-green)"/>
      <path d="M112 110 L140 138 L132 102 Z" fill="var(--bubble-green)"/>
    </svg>
    <div class="bubble-text"><span>青い灯を</span><span>さがす</span></div>
  </div>

  <div class="title-main">旅の物語<br>です!</div>

  <div class="author">
    <span class="author-label">著者</span>
    <div class="author-org">ぽんたるべカフェ 占導師</div>
    <div class="author-name">千景（柴崎奈緒）</div>
  </div>

  <div class="lead-box">人生の波と家族との<br>ご縁をひもといて<br><em>薬を使わず</em>に治す</div>

  <section class="band">
    <div class="band-lead">「絶対に治る、<small>治ったら</small></div>
    <div class="band-line">同じように苦しんでいる人の為に役立つ</div>
    <div class="band-line">本を書こう」…と決めていました。</div>
  </section>
</main>
</body>
</html>
```